Playful, Modern Brochure Design for informing about managed services provided

For our Managed Services we are looking for a brochure with simple explanation of the services we offer. Brochure not a full text brochure. Something like a summation with prices of the options we provide. Think about monitoring, VOIP, anti-virus, quillo 270 etc.

combination of Who We Are and products offering in a simple overview.

a bit similar to https://leaflet.pambervault.com/entry.aspx?id=8830412

it’s about professional services, security and stability of the customers IT, so the design should express that.

Target Market(s)

Business to Business

Font styles to use
Sans Serif
Other font styles liked:
• Arial

Colors

Designer to choose colors to be used in the design.

Requirements
Must have
• attractive front which invites to read further, inside summation of services.
• Contact Info
• Icons for services:
• Hosting, Security, Monitoring, Cloud, VOIP, Online Backup
Nice to have
• Other icons like Quillo 270, firewall, proxy server and other thinkable.
Should not have
• Pages with large amount of text.

```html
<!DOCTYPE html>
<html lang="en">
<head>
<meta charset="utf-8">
<title>Smart Network Solution – Brochure</title>
<link rel="stylesheet" href="https://fonts.googleapis.com/css2?family=Lato:wght@400;700&family=Roboto:wght@400;500&family=Roboto+Condensed:wght@700&family=Arimo:wght@400&display=swap">
<style>
  :root{
    --stage:#7f7f7f;
    --paper:#ffffff;
    --brand:#1f4fa0;
    --brand-bright:#2557a7;
    --brand-deep:#163f8c;
    --ink:#1e1e1e;
    --muted:#3a3a3a;
    --mist:#eef2f8;
  }
  *{box-sizing:border-box;margin:0;padding:0}
  html,body{width:1200px;height:1200px;overflow:hidden;background:var(--stage)}
  .canvas{position:relative;width:1200px;height:1200px}

  .page{position:absolute;background:var(--paper);overflow:hidden;box-shadow:0 8px 22px rgba(0,0,0,.35)}

  /* Front cover */
  .front{left:67px;top:257px;width:503px;height:686px}
  .front .photo{position:absolute;left:0;top:0;width:503px;height:363px;
    background:linear-gradient(160deg,#d9e3ef 0%,#a9c2e0 40%,#5f86c2 70%,#e6ecf3 100%)}
  .front .band{position:absolute;left:0;top:369px;width:503px;height:47px;
    background:linear-gradient(90deg,var(--brand-deep),var(--brand-bright) 50%,var(--brand-deep))}
  .front .lower{position:absolute;left:0;top:416px;width:503px;height:270px;
    background:linear-gradient(180deg,#fff,#f3f5f9)}
  .front .title{position:absolute;left:0;top:435px;width:503px;text-align:center;
    font-family:"Roboto",Arial,sans-serif;font-size:40px;color:var(--ink);font-weight:400;letter-spacing:-.3px}
  .front .title strong{font-family:"Roboto Condensed",Arial,sans-serif;font-weight:700;color:var(--brand)}
  .front .lead{position:absolute;left:0;top:490px;width:503px;text-align:center;
    font-family:"Lato",Arial,sans-serif;font-size:15px;line-height:20px;color:var(--ink)}
  .contact{position:absolute;left:47px;top:562px;font-family:"Lato",Arial,sans-serif}
  .contact h3{font-size:17px;font-weight:400;color:var(--brand);margin-bottom:8px}
  .contact li{list-style:none;display:flex;align-items:center;gap:12px;font-size:14px;color:var(--ink);height:23px}
  .contact svg{width:12px;height:12px;fill:var(--brand)}
  .front .divider{position:absolute;left:277px;top:570px;width:1px;height:84px;background:var(--brand)}
  .front .brand-name{position:absolute;left:317px;top:594px;font-family:"Roboto",Arial,sans-serif;
    font-size:28px;font-weight:500;color:var(--brand);letter-spacing:.5px}

  /* Back page */
  .back{left:632px;top:259px;width:497px;height:698px}
  .back .header{position:absolute;left:0;top:0;width:497px;height:76px;background:var(--brand-bright);
    display:flex;align-items:center;justify-content:center;
    font-family:"Roboto",Arial,sans-serif;font-size:27px;font-weight:400;color:#fff;letter-spacing:.3px}
  .back .services-bg{position:absolute;left:0;top:76px;width:497px;height:370px;
    background:radial-gradient(ellipse at 45% 45%,#dfe7f2 0%,#f4f6fa 55%,#fbfcfd 100%)}
  .back h2{position:absolute;left:35px;top:94px;font-family:"Roboto",Arial,sans-serif;font-weight:400;
    font-size:27px;color:var(--ink)}
  .back h2 strong{font-family:"Roboto Condensed",Arial,sans-serif;font-weight:700;color:var(--brand)}
  .back .intro{position:absolute;left:36px;top:141px;width:410px;font-family:"Arimo",Arial,sans-serif;
    font-size:9.4px;line-height:11.8px;color:var(--ink)}
  .service{position:absolute;display:flex;align-items:center;gap:23px;
    font-family:"Lato",Arial,sans-serif;font-size:17px;color:var(--brand)}
  .service .badge{width:48px;height:48px;border-radius:50%;background:var(--brand);
    border:3px solid #fff;box-shadow:0 2px 5px rgba(0,0,0,.3);display:flex;align-items:center;justify-content:center}
  .service svg{width:24px;height:24px;fill:none;stroke:#fff;stroke-width:1.8;stroke-linecap:round;stroke-linejoin:round}

  .back .footer{position:absolute;left:0;top:446px;width:497px;height:252px;
    background:linear-gradient(180deg,#1a4594 0%,var(--brand-deep) 60%,#153a82 100%)}
  .extra{position:absolute;top:506px;width:140px;margin-left:-70px;text-align:center;
    font-family:"Lato",Arial,sans-serif;font-size:17px;color:#fff}
  .extra .badge{width:52px;height:52px;margin:0 auto 10px;border-radius:50%;background:#fff;
    border:3px solid var(--brand-bright);box-shadow:0 0 0 2px #fff;display:flex;align-items:center;justify-content:center}
  .extra svg{width:28px;height:28px;fill:none;stroke:var(--brand);stroke-width:1.8;stroke-linecap:round;stroke-linejoin:round}
  .back .web{position:absolute;left:0;top:617px;width:497px;text-align:center;
    font-family:"Lato",Arial,sans-serif;font-size:21px;color:#fff;display:flex;justify-content:center;align-items:center;gap:8px}
  .back .web svg{width:14px;height:14px;fill:none;stroke:#fff;stroke-width:1.5}
</style>
</head>
<body>
<div class="canvas">

  <section class="page front">
    <div class="photo" role="img" aria-label="Photo of a business team at a meeting table using phones and tablets beneath a glowing cloud"></div>
    <div class="band" role="img" aria-label="Blue band with a network pattern"></div>
    <div class="lower"></div>
    <h1 class="title">Smart <strong>Network Solution</strong></h1>
    <p class="lead">Lorem Ipsum is simply dummy text of the printing<br>and typesetting industry.</p>
    <div class="contact">
      <h3>Contact Now</h3>
      <ul>
        <li><svg viewBox="0 0 24 24"><path d="M6.6 10.8a15 15 0 0 0 6.6 6.6l2.2-2.2a1 1 0 0 1 1-.25 11.4 11.4 0 0 0 3.6.6 1 1 0 0 1 1 1V20a1 1 0 0 1-1 1A17 17 0 0 1 3 4a1 1 0 0 1 1-1h3.5a1 1 0 0 1 1 1c0 1.25.2 2.45.6 3.6a1 1 0 0 1-.25 1z"/></svg>xxx-xxxx-xx</li>
        <li><svg viewBox="0 0 24 24"><path d="M2 9l10-6 10 6v11H2z M4 10l8 5 8-5" stroke="#fff" stroke-width="1.2"/></svg>hello@netvantra.io</li>
        <li><svg viewBox="0 0 24 24"><circle cx="12" cy="12" r="10"/></svg>www.netvantra.io</li>
      </ul>
    </div>
    <div class="divider"></div>
    <div class="brand-name">NETVANTRA</div>
  </section>

  <section class="page back">
    <div class="header">NETVANTRA</div>
    <div class="services-bg" role="img" aria-label="Faint background image of hands holding a globe with network connections"></div>
    <h2>Services &amp; <strong>Solutions</strong></h2>
    <p class="intro">Lorem Ipsum is simply dummy text of the printing and typesetting industry. Lorem Ipsum has been the industry's standard dummy text ever since the 1500s, when an unknown printer took a galley of type and scrambled it to make a type specimen book.</p>

    <div class="service" style="left:34px;top:220px">
      <span class="badge"><svg viewBox="0 0 24 24"><rect x="3" y="4" width="12" height="4"/><rect x="3" y="10" width="12" height="4"/><rect x="3" y="16" width="12" height="4"/><circle cx="18.5" cy="8" r="3.5"/></svg></span>Hosting</div>
    <div class="service" style="left:34px;top:298px">
      <span class="badge"><svg viewBox="0 0 24 24"><path d="M12 3l7 3v6c0 4-3 7-7 9-4-2-7-5-7-9V6z"/><path d="M9 12l2 2 4-4"/></svg></span>Security</div>
    <div class="service" style="left:34px;top:371px">
      <span class="badge"><svg viewBox="0 0 24 24"><rect x="3" y="4" width="18" height="12" rx="1"/><path d="M9 20h6M12 16v4"/><circle cx="15" cy="10" r="3"/><path d="M6 8h4M6 11h3"/></svg></span>Monitoring</div>
    <div class="service" style="left:278px;top:220px">
      <span class="badge"><svg viewBox="0 0 24 24"><rect x="10" y="3" width="4" height="3"/><rect x="3" y="10" width="4" height="3"/><rect x="17" y="10" width="4" height="3"/><rect x="10" y="17" width="4" height="3"/><circle cx="12" cy="11.5" r="2"/><path d="M12 6v3.5M7 11.5h3M14 11.5h3M12 13.5V17"/></svg></span>Cloud</div>
    <div class="service" style="left:278px;top:298px">
      <span class="badge"><svg viewBox="0 0 24 24"><path d="M7 18a4 4 0 0 1 0-8 5 5 0 0 1 10 0 4 4 0 0 1 0 8z"/><path d="M12 17v-6M9.5 13.5L12 11l2.5 2.5"/></svg></span>VOIP</div>
    <div class="service" style="left:278px;top:371px">
      <span class="badge"><svg viewBox="0 0 24 24"><rect x="3" y="4" width="18" height="12" rx="1"/><path d="M9 20h6M12 16v4"/><path d="M9 8l2 0 1 2-1 1a4 4 0 0 0 2 2l1-1 2 1v2"/></svg></span>Online Backup</div>

    <div class="footer" role="img" aria-label="Deep blue background with faint financial charts and figures"></div>
    <div class="extra" style="left:95px">
      <div class="badge"><svg viewBox="0 0 24 24"><circle cx="12" cy="7" r="3.5"/><path d="M5 21v-3a7 7 0 0 1 14 0v3z"/><path d="M12 14v5"/></svg></div>Quillo 270</div>
    <div class="extra" style="left:242px">
      <div class="badge"><svg viewBox="0 0 24 24"><path d="M12 3l6 2.5v5c0 3.5-2.5 6-6 7.5-3.5-1.5-6-4-6-7.5v-5z" fill="#1f4fa0"/><path d="M3 21h18M12 18v3"/></svg></div>Firewall</div>
    <div class="extra" style="left:383px">
      <div class="badge"><svg viewBox="0 0 24 24"><rect x="4" y="4" width="14" height="16"/><path d="M7 8h5M7 11h8M7 14h8M7 17h8M19 9V3M17 5l2-2 2 2"/></svg></div>Proxy Server</div>

    <div class="web"><svg viewBox="0 0 24 24"><circle cx="12" cy="12" r="10"/><path d="M2 12h20M12 2c3 3 3 17 0 20M12 2c-3 3-3 17 0 20"/></svg>www.netvantra.io</div>
  </section>

</div>
</body>
</html>
```